Medical Billing - Professional Marketing Flier

We are needing help designing a clean and professional looking easy to read marketing flier for a medical billing practice. The text needs to be large enough to print. We are looking for a 5.5 x 8.5 design that we can edit the text as needed. I have included our logo and what we initially want it to say. Please keep in mind, we also want our logo and contact details on the flier. Let me know if you have any questions.

```html
<!DOCTYPE html>
<html lang="en">
<head>
<meta charset="utf-8">
<title>Medical Billing Flier</title>
<link rel="stylesheet" href="https://fonts.googleapis.com/css2?family=Cinzel:wght@400;700&family=Tinos:wght@400;700&display=swap">
<style>
  :root{
    --backdrop:#efe4d6;
    --paper:#ffffff;
    --pink:#c763a3; --pink-soft:#f6e5ef;
    --purple:#7661a8; --purple-soft:#e9e4f1;
    --blue:#1b7bc1; --blue-soft:#dbe8f4;
    --navy:#1f56a3; --navy-soft:#dde4f0;
    --ink:#2b2b33;
    --band-start:#1aa3dd; --band-end:#1a55a3;
  }
  *{margin:0;padding:0;box-sizing:border-box}
  html,body{width:999px;height:1200px;overflow:hidden;background:var(--backdrop)}
  .flier{position:absolute;left:111px;top:0;width:776px;height:1200px;background:var(--paper);overflow:hidden}
  .hero{position:absolute;left:0;top:0;width:776px;height:259px;
    background:linear-gradient(110deg,#d9dde3 0%,#eef0f3 30%,#c9d7e8 55%,#6d9fd6 80%,#4d86c9 100%)}
  .hero-title{position:absolute;left:0;right:0;top:98px;text-align:center;
    font-family:'Cinzel',serif;font-weight:400;font-size:33px;line-height:46px;color:#fff;
    text-shadow:0 2px 6px rgba(20,30,60,.55)}
  .hero-band{position:absolute;left:0;top:259px;width:776px;height:10px;
    background:linear-gradient(90deg,var(--band-start),var(--band-end))}
  .service{position:absolute;left:0;width:776px;height:174px}
  .service .tab{position:absolute;left:0;top:0;width:172px;height:174px;border-radius:0 87px 87px 0}
  .service .badge{position:absolute;left:30px;top:25px;width:124px;height:124px;border-radius:50%;
    background:#fff;display:flex;align-items:center;justify-content:center}
  .service .copy{position:absolute;left:188px;top:9px;width:548px}
  .service h2{font-family:'Tinos',serif;font-weight:700;font-size:25px;line-height:28px;margin-bottom:3px}
  .service p{font-family:'Tinos',serif;font-size:15.6px;line-height:21.4px;color:var(--ink);text-align:justify}
  .billing{top:306px;background:var(--pink-soft)} .billing .tab{background:var(--pink)} .billing h2{color:var(--pink)}
  .aging{top:494px;background:var(--purple-soft)} .aging .tab{background:var(--purple)} .aging h2{color:var(--purple)}
  .credentialing{top:682px;background:var(--blue-soft)} .credentialing .tab{background:var(--blue)} .credentialing h2{color:var(--blue)}
  .contact{top:870px;background:var(--navy-soft)} .contact .tab{background:var(--navy)} .contact h2{color:var(--navy)} .contact .copy{top:18px}
  .brand{position:absolute;left:65px;top:1106px;font-family:'Tinos',serif;font-size:27px;color:var(--purple);letter-spacing:1px;display:flex;align-items:center;gap:10px}
  .brand .dot{width:14px;height:14px;border-radius:50%;background:var(--purple)}
  .details{position:absolute;right:36px;top:1073px;text-align:right;border-top:2px solid #333;padding-top:6px}
  .details p{font-family:'Tinos',serif;font-size:21px;line-height:27px;color:var(--ink)}
  .details-rule-fix{}
</style>
</head>
<body>
<main class="flier">
  <header>
    <div class="hero" role="img" aria-label="Photo of a clinician in blue scrubs writing on a clipboard medical chart"></div>
    <h1 class="hero-title">MEDICAL BILLING TAILORED TO<br>YOUR PRACTICES NEEDS</h1>
    <div class="hero-band"></div>
  </header>

  <section class="service billing">
    <div class="tab"><div class="badge">
      <svg width="56" height="62" viewBox="0 0 56 62" fill="none" stroke="var(--pink)" stroke-width="3">
        <rect x="4" y="8" width="34" height="46" rx="3"/>
        <rect x="14" y="3" width="14" height="9" rx="2"/>
        <path d="M21 18v12M15 24h12" stroke-width="4"/>
        <path d="M10 36h22M10 42h14M10 48h12"/>
        <ellipse cx="45" cy="44" rx="8" ry="3"/><path d="M37 44v10c0 2 16 2 16 0V44M37 49c0 2 16 2 16 0"/>
        <ellipse cx="33" cy="50" rx="6" ry="2.5"/><path d="M27 50v6c0 2 12 2 12 0v-6"/>
      </svg>
    </div></div>
    <div class="copy">
      <h2>MEDICAL BILLING</h2>
      <p>Would you prefer to spend time focusing on your clients and running your practice rather than trying to stay up to speed with the constantly changing medical billing rules and regulations? Let us help you by managing your medical billing and dealing with the insurance companies on your behalf! We work with you to tailor the entire medical billing process to suit your practices needs while making it as smooth and painless as possible.</p>
    </div>
  </section>

  <section class="service aging">
    <div class="tab"><div class="badge">
      <svg width="40" height="64" viewBox="0 0 40 64" fill="none" stroke="var(--purple)" stroke-width="5" stroke-linejoin="round">
        <path d="M4 3h32v12L20 32 36 49v12H4V49l16-17L4 15z"/>
        <path d="M10 57l10-11 10 11z" fill="var(--purple)" stroke-width="2"/>
      </svg>
    </div></div>
    <div class="copy">
      <h2>AGING</h2>
      <p>Are you leaving money on the table? Are you able to do the follow-through needed to keep your aging in check and more money flowing into your practice? Are you uncertain about how to get insurance to pay on claims that should be covered but for some reason they decided not to? We can clean up your aging, reduce the amount of time it takes for claims to pay out, and we can keep your aging to a minimum.</p>
    </div>
  </section>

  <section class="service credentialing">
    <div class="tab"><div class="badge">
      <svg width="62" height="70" viewBox="0 0 62 70" fill="none" stroke="var(--blue)" stroke-width="3" stroke-linejoin="round">
        <path d="M31 3l6 5 8-1 3 7 7 4-1 8 5 6-5 6 1 8-7 4-3 7-8-1-6 5-6-5-8 1-3-7-7-4 1-8-5-6 5-6-1-8 7-4 3-7 8 1z"/>
        <circle cx="31" cy="33" r="14"/>
        <path d="M23 33l6 6 14-17" stroke-width="4"/>
        <path d="M16 55l-6 12 8-3 4 6 5-11M46 55l6 12-8-3-4 6-5-11"/>
      </svg>
    </div></div>
    <div class="copy">
      <h2>CREDENTIALING</h2>
      <p>Are you wanting to get contracted with insurance companies but aren’t sure how to go about it? Are you wanting to expand your client base by having the option to bill insurance? Let us take the confusion out of what can seem like a daunting task! We can get you and your practitioners contracted with the insurance companies of your choice and help you navigate through the process every step of the way!</p>
    </div>
  </section>

  <section class="service contact">
    <div class="tab"><div class="badge">
      <svg width="82" height="58" viewBox="0 0 82 58" fill="none">
        <rect x="24" y="6" width="52" height="42" stroke="var(--navy)" stroke-width="3"/>
        <path d="M24 6l26 24 26-24M24 48l18-18M76 48L58 30" stroke="var(--navy)" stroke-width="3"/>
        <path d="M8 8c3-3 7-3 9 0l5 8c1 3 0 5-3 7l-3 2c2 7 7 12 14 15l3-3c2-2 5-2 7 0l6 5c2 2 2 5-1 8-6 6-16 4-26-5S0 17 8 8z" fill="var(--navy)"/>
      </svg>
    </div></div>
    <div class="copy">
      <h2>CONTACT US</h2>
      <p>If any of these processes are something you would like our help with or to consult with us on, please email us or give us a call! We specialize in billing and contracting for Nutritionists and Dietitians. We would love to help you expand your business and take the pain and frustration out of billing so you can focus on your clients.</p>
    </div>
  </section>

  <footer>
    <div class="brand"><span class="dot"></span>Vela Medical Billing</div>
    <div class="details">
      <p>Company Office Address</p>
      <p>Phone No: 000 111 222</p>
      <p>Email : your@emailaddress</p>
    </div>
  </footer>
</main>
</body>
</html>
```